Label for Refill packaging eco-conscious beauty brand

We need a label for our refill pouch. Velvet Harbor is an unscented conditioner formulated using the finest healthy & pure ingredients, free of chemicals and harmful toxins. As a minimalist beauty brand we are proud to be certified with TQB, Norvamark and Silver Kestrel.

We already have the pouches and an exciting label for our regular bottles.
We choose a kraft brown packing for the refill pouch and would like something minimalist but elegant for the label.

```html
<!DOCTYPE html>
<html lang="en">
<head>
<meta charset="utf-8">
<title>Velvet Harbor – Refill Label</title>
<link rel="stylesheet" href="https://fonts.googleapis.com/css2?family=Montserrat:wght@200;300;400;500;600&display=swap">
<style>
  :root {
    --page-bg: #ffffff;
    --label-plum: #8a6c71;
    --label-vein: #977c81;
    --label-ink: #f4eeea;
  }
  html, body {
    margin: 0;
    padding: 0;
    width: 1200px;
    height: 1200px;
    overflow: hidden;
    background: var(--page-bg);
  }
  .canvas {
    position: relative;
    width: 1200px;
    height: 1200px;
  }
  .refill-label {
    position: absolute;
    left: 0;
    top: 0;
    width: 1200px;
    height: 1200px;
  }
  .label-disc { fill: var(--label-plum); }
  .leaf-texture { fill: url(#leafGlow); }
  .label-text {
    font-family: "Montserrat", sans-serif;
    fill: var(--label-ink);
    text-anchor: middle;
  }
  .brand-mark { fill: none; stroke: var(--label-ink); stroke-width: 2.5; }
  .brand-name { font-size: 38px; font-weight: 400; letter-spacing: 1px; }
  .product-name { font-size: 96px; font-weight: 500; letter-spacing: -1px; }
  .product-desc { font-size: 31px; font-weight: 300; letter-spacing: 1px; }
  .volume { font-size: 37px; font-weight: 600; }
  .refill-word { font-size: 100px; font-weight: 200; letter-spacing: 2px; }
</style>
</head>
<body>
<main class="canvas">
  <svg class="refill-label" viewBox="0 0 1200 1200" xmlns="http://www.w3.org/2000/svg">
    <defs>
      <radialGradient id="leafGlow" cx="50%" cy="55%" r="50%">
        <stop offset="0%" stop-color="#967b80" stop-opacity="0.9"/>
        <stop offset="100%" stop-color="#8a6c71" stop-opacity="0"/>
      </radialGradient>
    </defs>

    <circle class="label-disc" cx="600" cy="600" r="450"/>
    <ellipse class="leaf-texture" cx="600" cy="640" rx="360" ry="400"
             role="img" aria-label="Faint leaf-skeleton vein pattern behind the label text"/>

    <g class="brand">
      <circle class="brand-mark" cx="600" cy="250" r="34"/>
      <text class="label-text brand-name" x="600" y="352">LUMA</text>
      <text class="label-text brand-name" x="600" y="396">Elin</text>
    </g>

    <g class="product">
      <text class="label-text product-name" x="600" y="510">Velvet</text>
      <text class="label-text product-name" x="600" y="578">Harbor</text>
      <text class="label-text product-desc" x="600" y="651">unscented hair conditioner</text>
      <text class="label-text product-desc" x="600" y="689">après - shampoing non parfumé</text>
    </g>

    <text class="label-text volume" x="600" y="813">238 ml ℮, /</text>
    <text class="label-text refill-word" x="600" y="942">Refill</text>
  </svg>
</main>
</body>
</html>
```